Quillory Nest Business Card

I need a business card design. We are a collaborate online training company. Our colors are gray and green. Our website is QuilloryNest.com

I would like an area for a profile picture within the card

```html
<!DOCTYPE html>
<html lang="en">
<head>
<meta charset="UTF-8">
<title>Quillory Nest Business Card</title>
<link rel="stylesheet" href="https://fonts.googleapis.com/css2?family=Source+Sans+3:wght@400;600;700&display=swap">
<style>
  :root {
    --backdrop: #8a8a8a;
    --brand-green: #7dbd2f;
    --paper: #efefef;
    --ink: #2b2b2b;
    --panel-dark: #000000;
    --white: #ffffff;
    --ring: #d9d9d9;
    --photo-light: #c9ccd0;
    --photo-dark: #4a4e55;
  }
  * { box-sizing: border-box; margin: 0; padding: 0; }
  html, body {
    width: 1200px;
    height: 960px;
    overflow: hidden;
  }
  body {
    background: var(--backdrop);
    font-family: "Source Sans 3", "Myriad Pro", sans-serif;
    position: relative;
  }
  .card {
    position: absolute;
    left: 250px;
    width: 700px;
    height: 400px;
    box-shadow: 0 6px 18px rgba(0,0,0,0.25);
    overflow: hidden;
  }
  .card--front { top: 50px; background: var(--brand-green); }
  .card--back  { top: 510px; display: flex; }

  .front-brand {
    position: absolute;
    inset: 0;
    display: flex;
    align-items: center;
    justify-content: center;
    gap: 18px;
  }
  .brand-dot {
    width: 46px;
    height: 46px;
    border-radius: 50%;
    background: var(--white);
  }
  .front-brand .brand-name {
    color: var(--white);
    font-size: 58px;
    font-weight: 600;
    letter-spacing: -0.5px;
  }

  .back-info {
    width: 52%;
    background: var(--paper);
    padding: 40px 36px;
    display: flex;
    flex-direction: column;
    justify-content: space-between;
  }
  .back-brand {
    display: flex;
    align-items: center;
    gap: 12px;
  }
  .back-brand .brand-dot {
    width: 26px;
    height: 26px;
    background: var(--brand-green);
  }
  .back-brand .brand-name {
    color: var(--brand-green);
    font-size: 32px;
    font-weight: 600;
    letter-spacing: -0.3px;
  }
  .contact-list {
    list-style: none;
    display: flex;
    flex-direction: column;
    gap: 8px;
    margin-bottom: 10px;
  }
  .contact-item {
    display: flex;
    align-items: center;
    gap: 14px;
    color: var(--ink);
    font-size: 19px;
  }
  .contact-icon { width: 18px; height: 18px; flex: none; }

  .back-profile {
    flex: 1;
    background: var(--panel-dark);
    display: flex;
    flex-direction: column;
    align-items: center;
    padding-top: 52px;
    color: var(--white);
  }
  .profile-photo {
    width: 150px;
    height: 150px;
    border-radius: 50%;
    border: 7px solid var(--ring);
    background: radial-gradient(circle at 50% 40%, var(--photo-light) 0%, var(--photo-dark) 100%);
  }
  .profile-name {
    margin-top: 86px;
    font-size: 27px;
    font-weight: 700;
  }
  .profile-title {
    font-size: 19px;
    margin-top: 2px;
  }
</style>
</head>
<body>
  <section class="card card--front" aria-label="Card front">
    <div class="front-brand">
      <span class="brand-dot"></span>
      <span class="brand-name">QuilloryNest</span>
    </div>
  </section>

  <section class="card card--back" aria-label="Card back">
    <div class="back-info">
      <div class="back-brand">
        <span class="brand-dot"></span>
        <span class="brand-name">QuilloryNest</span>
      </div>
      <ul class="contact-list">
        <li class="contact-item">
          <svg class="contact-icon" viewBox="0 0 24 24" aria-hidden="true"><path fill="#555" d="M6.6 10.8a15.1 15.1 0 0 0 6.6 6.6l2.2-2.2a1 1 0 0 1 1-.25 11.4 11.4 0 0 0 3.6.57 1 1 0 0 1 1 1V20a1 1 0 0 1-1 1A17 17 0 0 1 3 4a1 1 0 0 1 1-1h3.5a1 1 0 0 1 1 1c0 1.25.2 2.45.57 3.6a1 1 0 0 1-.25 1z"/></svg>
          <span>000-000-0000</span>
        </li>
        <li class="contact-item">
          <svg class="contact-icon" viewBox="0 0 24 24" aria-hidden="true"><rect x="2" y="5" width="20" height="14" rx="2" fill="#555"/><path d="M3 6l9 7 9-7" fill="none" stroke="#efefef" stroke-width="1.8"/></svg>
          <span>abcd@quillorynest.com</span>
        </li>
        <li class="contact-item">
          <svg class="contact-icon" viewBox="0 0 24 24" aria-hidden="true"><circle cx="12" cy="12" r="10" fill="#555"/><path d="M2 12h20M12 2c3 3 3 17 0 20M12 2c-3 3-3 17 0 20" fill="none" stroke="#efefef" stroke-width="1.3"/></svg>
          <span>www.quillorynest.com</span>
        </li>
      </ul>
    </div>
    <div class="back-profile">
      <div class="profile-photo" role="img" aria-label="Profile photo of the card holder"></div>
      <p class="profile-name">Your Name</p>
      <p class="profile-title">Job Title</p>
    </div>
  </section>
</body>
</html>
```